U.S. Popcorn company needs business cards

We are a popcorn company that manufactures popcorn and sells it to grocery stores worldwide. Our theme is "Americana" and our logo is Kettle Mesa Byway which is the most famous highway in the U.S.

We would like the design to be simple and to use both sides. On the back side we would like to see just the logo and website. The front would be normal details

Target Market(s)

Wholesalers, grocers and distributors

Industry/Entity Type

Manufacture

Contact Information for Business Card

Business name: Kettle Mesa Popcorn
Phone: +1 555 014 2286
Email: Dale@kettlemesapopcorn.com
website: www.kettlemesapopcorn.com
Tag Line: "POPular for a reason"
Name: Dale Whitcombe
Title: Founder/President

Requirements
Must have
• Either this design should be fun or clean and simple. I will let you show me your thougths.
Nice to have
• Anything that ties in the real Kettle Mesa Byway.
• Colors might need to be red, white and blue incorporated.
Should not have
• Not be too busy.

```html
<!DOCTYPE html>
<html lang="en">
<head>
<meta charset="utf-8">
<title>Kettle Mesa Popcorn – Business Card</title>
<link href="https://fonts.googleapis.com/css2?family=Source+Sans+3:ital,wght@0,400;0,600;0,700;1,700&display=swap" rel="stylesheet">
<style>
  :root {
    --navy: #0b2a6b;
    --red: #e0262c;
    --white: #ffffff;
    --backdrop: #584737;
    --text-light: #f2f4fa;
  }
  * { margin: 0; padding: 0; box-sizing: border-box; }
  html, body { width: 1200px; height: 987px; overflow: hidden; }
  body {
    background: var(--backdrop);
    font-family: "Source Sans 3", Arial, sans-serif;
    position: relative;
  }
  .card {
    position: absolute;
    left: 293px;
    width: 615px;
    height: 350px;
    background: var(--white);
    overflow: hidden;
    box-shadow: 0 3px 8px rgba(0,0,0,0.35);
  }
  .card--front { top: 130px; }
  .card--back { top: 505px; }

  .front-wave { position: absolute; inset: 0; width: 615px; height: 350px; }

  .brand-name {
    position: absolute;
    width: 220px;
    text-align: center;
    color: var(--navy);
    font-weight: 700;
    text-transform: uppercase;
    line-height: 1.05;
    letter-spacing: 0.5px;
  }
  .card--front .brand-name { left: 31px; top: 138px; font-size: 30px; }
  .card--back .brand-name { left: 197px; top: 120px; font-size: 34px; }

  .contact-block { position: absolute; left: 331px; top: 98px; color: var(--text-light); }
  .person-name { color: var(--red); font-size: 21px; font-weight: 600; line-height: 1.2; }
  .person-title { font-size: 16.5px; line-height: 1.2; margin-bottom: 19px; }
  .contact-list { list-style: none; }
  .contact-list li {
    display: flex; align-items: center;
    font-size: 15.5px; line-height: 23.5px;
  }
  .contact-list svg { width: 13px; height: 13px; margin-right: 9px; flex: none; }

  .tagline {
    position: absolute;
    left: 0; right: 0; top: 300px;
    text-align: center;
    color: var(--navy);
    font-size: 18.5px;
    font-weight: 700;
    font-style: italic;
  }
  .tagline .tagline-caps { font-style: normal; }
</style>
</head>
<body>

<section class="card card--front" aria-label="Business card front">
  <svg class="front-wave" viewBox="0 0 525 299" preserveAspectRatio="none" aria-hidden="true">
    <path fill="var(--navy)" d="M283 0 C250 25 225 40 230 70 C235 110 250 140 246 175 C242 205 225 225 240 255 C260 285 330 290 375 299 L525 299 L525 0 Z"/>
    <path fill="none" stroke="var(--red)" stroke-width="1.6" d="M277 0 C243 25 218 40 223 70 C228 110 243 140 239 175 C235 205 217 226 233 258 C253 290 322 292 366 299"/>
  </svg>

  <div class="brand-name">Kettle Mesa<br>Popcorn</div>

  <div class="contact-block">
    <p class="person-name">Dale Whitcombe</p>
    <p class="person-title">Founder/President</p>
    <ul class="contact-list">
      <li>
        <svg viewBox="0 0 16 16" aria-hidden="true"><path fill="var(--red)" d="M3.6 1.2l2.3 2.6-1.3 2c.9 1.9 2.3 3.4 4.3 4.4l2-1.3 2.6 2.3-1.4 2.4C7 13.5 2.6 9.1 1.2 3.3z"/></svg>
        +1 555 014 2286
      </li>
      <li>
        <svg viewBox="0 0 16 16" aria-hidden="true"><rect x="1" y="3" width="14" height="10" fill="var(--red)"/><path d="M1.5 3.5L8 9l6.5-5.5" fill="none" stroke="var(--navy)" stroke-width="1.3"/></svg>
        Dale@kettlemesapopcorn.com
      </li>
      <li>
        <svg viewBox="0 0 16 16" aria-hidden="true"><circle cx="8" cy="8" r="7" fill="var(--red)"/><path d="M1 8h14M8 1c-3 3.5-3 10.5 0 14M8 1c3 3.5 3 10.5 0 14" fill="none" stroke="var(--navy)" stroke-width="1.1"/></svg>
        www.kettlemesapopcorn.com
      </li>
    </ul>
  </div>
</section>

<section class="card card--back" aria-label="Business card back">
  <div class="brand-name">Kettle Mesa<br>Popcorn</div>
  <p class="tagline"><span class="tagline-caps">POP</span>ular for a reason</p>
</section>

</body>
</html>
```